Corvane Business Cards & Staionary
Corvane, Inc.
Project: Corvane Business Cards & Staionary
Corvane Business Cards & Staionary - Real Estate
Creative Brief
Professional
Leonard T. Haskovich
President
418 W. Thornberry Blvd. Harlow, TX 75902
len@corvanetx.com

```html
<!DOCTYPE html>
<html lang="en">
<head>
<meta charset="utf-8">
<title>Corvane, Inc. – Business Cards</title>
<link href="https://fonts.googleapis.com/css2?family=Cinzel:wght@400;600;700&display=swap" rel="stylesheet">
<style>
  :root {
    --gold: #d09a1c;
    --gold-light: #e9bd45;
    --gold-dark: #a8770e;
    --white: #ffffff;
    --ink: #4a4a4a;
    --stage: #e4e4e2;
  }
  * { margin: 0; padding: 0; box-sizing: border-box; }
  html, body { width: 1200px; height: 838px; overflow: hidden; }
  body {
    background: var(--stage);
    font-family: "Cinzel", serif;
    position: relative;
  }
  .card {
    position: absolute;
    top: 259px;
    width: 560px;
    height: 320px;
    box-shadow: 0 6px 18px rgba(0,0,0,.18);
    overflow: hidden;
  }
  /* Card back */
  .card-back {
    left: 620px;
    background: radial-gradient(circle at 35% 40%, var(--gold-light), var(--gold) 55%, var(--gold-dark));
  }
  .back-brand {
    position: absolute;
    left: 70px; top: 122px;
    display: flex; align-items: center; gap: 16px;
    color: var(--white);
    font-weight: 700;
    font-size: 50px;
    letter-spacing: 2px;
  }
  .brand-square {
    width: 34px; height: 34px;
    background: var(--white);
  }
  .back-web {
    position: absolute;
    right: 30px; bottom: 34px;
    color: var(--white);
    font-size: 15px;
    letter-spacing: 3px;
  }
  /* Card front */
  .card-front {
    left: 20px;
    background: var(--white);
    display: flex;
  }
  .front-info {
    width: 50%;
    background: linear-gradient(135deg, var(--gold-light), var(--gold) 60%, var(--gold-dark));
    color: var(--white);
    position: relative;
  }
  .front-info::after {
    content: "";
    position: absolute;
    inset: 14px 0 14px 14px;
    border: 1.5px solid var(--white);
    border-right: none;
  }
  .person { position: absolute; left: 40px; top: 40px; }
  .person-name { font-size: 16px; font-weight: 600; letter-spacing: 1px; }
  .person-title { font-size: 11px; letter-spacing: 2px; margin-top: 4px; }
  .contact-list {
    list-style: none;
    position: absolute; left: 40px; top: 128px;
    font-size: 10.5px; letter-spacing: .5px;
  }
  .contact-list li { display: flex; align-items: center; gap: 9px; margin-bottom: 8px; }
  .contact-list svg { flex: none; }
  .front-logo {
    width: 50%;
    position: relative;
  }
  .logo-frame {
    position: absolute;
    inset: 14px 14px 14px 0;
    border: 1.5px solid var(--gold);
    border-left: none;
  }
  .logo-lockup {
    position: absolute;
    left: 0; right: 14px; top: 124px;
    display: flex; flex-direction: column; align-items: center;
  }
  .logo-name {
    display: flex; align-items: center; gap: 8px;
    color: var(--ink);
    font-weight: 700;
    font-size: 23px;
    white-space: nowrap;
  }
  .logo-square { width: 14px; height: 14px; background: var(--gold); }
  .logo-tagline {
    margin-top: 6px;
    font-size: 7.5px;
    letter-spacing: 1.2px;
    color: var(--ink);
    white-space: nowrap;
  }
</style>
</head>
<body>

<section class="card card-front">
  <div class="front-info">
    <div class="person">
      <p class="person-name">Leonard T. Haskovich</p>
      <p class="person-title">President</p>
    </div>
    <ul class="contact-list">
      <li>
        <svg width="14" height="14" viewBox="0 0 14 14"><circle cx="7" cy="7" r="7" fill="#fff"/><path d="M7 3a2.3 2.3 0 0 0-2.3 2.3C4.7 7 7 10.5 7 10.5S9.3 7 9.3 5.3A2.3 2.3 0 0 0 7 3z" fill="#d09a1c"/></svg>
        <span>418 W. Thornberry Blvd.<br>Harlow, TX 75902</span>
      </li>
      <li>
        <svg width="14" height="14" viewBox="0 0 14 14"><circle cx="7" cy="7" r="7" fill="#fff"/><path d="M4.5 3.5l1.6-.3.8 2-1 .7a5 5 0 0 0 2.2 2.2l.7-1 2 .8-.3 1.6C8 10 4 6 4.5 3.5z" fill="#d09a1c"/></svg>
        <span>(555) 204-7731</span>
      </li>
      <li>
        <svg width="14" height="14" viewBox="0 0 14 14"><circle cx="7" cy="7" r="7" fill="#fff"/><rect x="4" y="5" width="6" height="4" fill="#d09a1c"/><rect x="5" y="3.5" width="4" height="2" fill="#d09a1c"/></svg>
        <span>(555) 204-7732</span>
      </li>
      <li>
        <svg width="14" height="14" viewBox="0 0 14 14"><circle cx="7" cy="7" r="7" fill="#fff"/><rect x="3.5" y="4.5" width="7" height="5" fill="#d09a1c"/><path d="M3.5 4.5L7 7.3l3.5-2.8" stroke="#fff" stroke-width=".8" fill="none"/></svg>
        <span>len@corvanetx.com</span>
      </li>
      <li>
        <svg width="14" height="14" viewBox="0 0 14 14"><circle cx="7" cy="7" r="7" fill="#fff"/><circle cx="7" cy="7" r="3" fill="#d09a1c"/></svg>
        <span>/corvanehomes</span>
      </li>
      <li>
        <svg width="14" height="14" viewBox="0 0 14 14"><circle cx="7" cy="7" r="7" fill="#fff"/><circle cx="7" cy="7" r="3.2" fill="none" stroke="#d09a1c" stroke-width="1"/><path d="M3.8 7h6.4M7 3.8v6.4" stroke="#d09a1c" stroke-width=".8"/></svg>
        <span>www.corvanetx.com</span>
      </li>
    </ul>
  </div>
  <div class="front-logo">
    <div class="logo-frame"></div>
    <div class="logo-lockup">
      <p class="logo-name"><span class="logo-square"></span>Corvane, Inc.</p>
      <p class="logo-tagline">Property Management &amp; Real Estate</p>
    </div>
  </div>
</section>

<section class="card card-back">
  <p class="back-brand"><span class="brand-square"></span>Corvane</p>
  <p class="back-web">www.corvanetx.com</p>
</section>

</body>
</html>
```